TKA Electricial Contracting Services

Hi guys, after a design for my small electrical company, have logo design files to be incorporated into the layout, the basic concept is electrical contracting services for residential, commercial, industrial & data services, image is clean clear and strong,

Card format is to have a nice clean logo on front,with maybe the Residential – commercial – industrial - data, followed with licensed & insured, followed by contact details on backside of the card.

Target Market(s)

Residential, commercial, industrial sectors.

Industry/Entity Type

Electrical

Contact Information for Business Card

TKA logo,
Residential – commercial – industrial - data
REC: 61372
Email: tka@poralink.net.au
Phone: 0458 203 719

Requirements
Must have
• Clean & strong design.
Nice to have
• If possible, I would like the logo colours inverted so the text is orange and the background is black on the front of the card, then the backside of the card be the reverse colour
Should not have
• No Sparks, lightning bolts,

```html
<!DOCTYPE html>
<html lang="en">
<head>
<meta charset="utf-8">
<title>TKA Electrical – Business Card</title>
<link rel="stylesheet" href="https://fonts.googleapis.com/css2?family=Exo+2:wght@500;600;700&display=swap">
<style>
  :root {
    --page: #f8f9fd;
    --black: #000000;
    --orange: #f5842c;
    --shadow: rgba(0, 0, 0, 0.35);
  }
  * { margin: 0; padding: 0; box-sizing: border-box; }
  html, body {
    width: 1200px;
    height: 1000px;
    overflow: hidden;
    background: var(--page);
    font-family: "Exo 2", sans-serif;
  }
  .stage { position: relative; width: 1200px; height: 1000px; }

  .card {
    position: absolute;
    width: 735px;
    height: 419px;
    box-shadow: 4px 5px 8px var(--shadow);
  }
  .card--front { left: 365px; top: 52px; background: var(--black); color: var(--orange); }
  .card--back  { left: 80px;  top: 516px; background: var(--orange); color: var(--black); }

  /* Business name placeholder */
  .brand-name {
    position: absolute;
    font-weight: 600;
    white-space: nowrap;
    text-align: center;
    line-height: 1;
  }
  .card--front .brand-name {
    left: 0; right: 0; top: 165px;
    font-size: 42px;
    letter-spacing: 0.5px;
  }
  .card--back .brand-name {
    left: 134px; width: 160px; top: 198px;
    font-size: 18px;
  }

  .services {
    position: absolute;
    left: 0; right: 0; top: 324px;
    text-align: center;
    font-weight: 600;
  }
  .services__list { font-size: 20.5px; letter-spacing: 0.8px; }
  .services__cred { font-size: 17.5px; letter-spacing: 1.2px; text-transform: uppercase; margin-top: 1px; }

  .contact { position: absolute; left: 383px; top: 157px; font-weight: 700; }
  .contact__licence { font-size: 23px; letter-spacing: 1.5px; margin-bottom: 4px; }
  .contact__line { display: flex; align-items: center; height: 36px; }
  .contact__icon { width: 30px; margin-left: 10px; margin-right: 25px; display: flex; justify-content: center; }
  .contact__email { font-size: 22px; font-weight: 600; }
  .contact__phone { font-size: 25px; letter-spacing: 0.5px; }
</style>
</head>
<body>
<main class="stage">

  <section class="card card--front" aria-label="Card front">
    <p class="brand-name">Tara Kell Electrical</p>
    <div class="services">
      <p class="services__list">residential - commercial - industrial - data</p>
      <p class="services__cred">Licensed &amp; Insured</p>
    </div>
  </section>

  <section class="card card--back" aria-label="Card back">
    <p class="brand-name">Tara Kell Electrical</p>
    <div class="contact">
      <p class="contact__licence">REC. 61372</p>
      <p class="contact__line">
        <span class="contact__icon">
          <svg width="30" height="20" viewBox="0 0 30 20" aria-hidden="true">
            <rect x="0" y="0" width="30" height="20" fill="var(--black)"/>
            <polyline points="1,1 15,12 29,1" fill="none" stroke="var(--orange)" stroke-width="1.6"/>
            <line x1="1" y1="19" x2="11" y2="9" stroke="var(--orange)" stroke-width="1.4"/>
            <line x1="29" y1="19" x2="19" y2="9" stroke="var(--orange)" stroke-width="1.4"/>
          </svg>
        </span>
        <span class="contact__email">tka@poralink.net.au</span>
      </p>
      <p class="contact__line">
        <span class="contact__icon">
          <svg width="28" height="34" viewBox="0 0 28 34" aria-hidden="true">
            <path d="M6 1 L11 9 L8 12 C9 17 13 22 17 25 L20 22 L27 28 L22 33 C12 31 2 19 1 6 Z" fill="var(--black)"/>
          </svg>
        </span>
        <span class="contact__phone">0458 203 719</span>
      </p>
    </div>
  </section>

</main>
</body>
</html>
```